Company Values - print for wall

We ned a print of our values on one of the walls in our office. Create a couple of suggestions that we can print on our walls.

Summary:
- See power point with values
- make two suggestion: one with only titles + one with titles and bulletpoints / use the "We" version)
- make a suggestion in a moon raiders theme
- see brand book for inspiration
- see images of office for inspiration
Updates

The company's values that we want to highlight are: 1. Exceed expectations 2. Execute with passion 3. Empower each other Exceed expectations:​ • We establish a good understanding of current expectations.​ • We provide helpful, honest, and timely feedback.​ • We deliver impressive quality.​ Execute with passion:​ • We embrace change.​ • We seek innovative solutions.​ • We inspire others with your actions and attitudes. ​ • We care about success. ​ • We are confident and humble. Empower each other:​ • We are available to help colleagues.​ • We are open-minded.​ • We seek and share information proactively.​ • We respect others’ time.​ This is in line with achieving the company vision: « Our vision is to make a difference for our customers through our highly customizable solutions for planning, execution, and analysis. It’s less about the software itself and more about customer success. Make better decisions faster with Clearmont. »​ Eirik Tove Malmberg, CEO Clearmont Company slogan: Better Decisions Faster​ It's a lot of text above, but what we what to emphasize most are the following text above and here again: exceed expectations, execute with passion, empower each other We can do something fun and cool with the Moon Raiders theme as this is internal - that's the visual that would work with the company culture.

Font styles to use
Sans Serif

Requirements
Nice to have
• - one suggestion with Montserrat font
- one suggestion in moon raiders font

```html
<!DOCTYPE html>
<html lang="en">
<head>
<meta charset="utf-8">
<title>Company Values – Wall Print</title>
<link rel="stylesheet" href="https://fonts.googleapis.com/css2?family=Montserrat:wght@500&family=Orbitron:wght@500;900&display=swap">
<style>
  :root {
    --bg: #020409;
    --teal: #1fb5b8;
    --red: #e8514f;
    --orange: #f0913a;
    --ink: #f4f4f6;
    --glow: #2a6fa8;
  }
  * { margin: 0; padding: 0; box-sizing: border-box; }
  html, body { width: 1200px; height: 1200px; overflow: hidden; background: var(--bg); }
  .poster { position: relative; width: 1200px; height: 1200px; background: var(--bg); overflow: hidden; }

  .scene-figure {
    position: absolute; left: 620px; top: 160px; width: 600px; height: 700px;
    background: radial-gradient(ellipse closest-side at 55% 45%, rgba(40,50,110,0.45) 0%, rgba(20,24,60,0.25) 45%, rgba(2,4,9,0) 100%);
  }
  .scene-blade {
    position: absolute; left: 400px; top: 560px; width: 240px; height: 220px;
    background: radial-gradient(ellipse closest-side at 60% 55%, rgba(40,190,90,0.42) 0%, rgba(30,90,60,0.15) 50%, rgba(2,4,9,0) 100%);
  }
  .emblem-glow {
    position: absolute; border-radius: 50%;
    background: radial-gradient(circle closest-side, rgba(80,160,230,0.35) 0%, rgba(42,111,168,0.18) 55%, rgba(2,4,9,0) 100%);
  }
  .emblem-glow--top { left: 990px; top: 118px; width: 140px; height: 140px; }
  .emblem-glow--left { left: 166px; top: 552px; width: 160px; height: 160px; }
  .emblem-glow--bottom { left: 814px; top: 946px; width: 140px; height: 140px; }

  .value-title { position: absolute; overflow: visible; }
  .value-title text { font-family: "Orbitron", sans-serif; }
  .value-title .headline { font-weight: 500; fill: none; stroke-width: 2; }
  .value-title .subline { font-weight: 900; }

  .value--exceed { --accent: var(--teal); }
  .value--empower { --accent: var(--red); }
  .value--execute { --accent: var(--orange); }
  .value-title .headline { stroke: var(--accent); }
  .value-title .subline { fill: var(--accent); }

  .value-points { position: absolute; list-style: none; }
  .value-points li {
    position: absolute; left: 0; white-space: nowrap;
    font-family: "Montserrat", sans-serif; font-weight: 500;
    font-size: 17px; line-height: 23px; letter-spacing: 0.3px; color: var(--ink);
  }
  .value-points li::before {
    content: ""; position: absolute; left: -38px; top: 2px;
    width: 20px; height: 20px; border-radius: 50%;
    border: 2px solid var(--accent);
  }
</style>
</head>
<body>
<main class="poster">
  <div class="scene-figure" role="img" aria-label="Dark illustration of a hooded figure in shadow"></div>
  <div class="scene-blade" role="img" aria-label="Glowing green energy blade held by the figure"></div>
  <div class="emblem-glow emblem-glow--top" role="img" aria-label="Glowing blue decorative emblem"></div>
  <div class="emblem-glow emblem-glow--left" role="img" aria-label="Glowing blue decorative emblem"></div>
  <div class="emblem-glow emblem-glow--bottom" role="img" aria-label="Glowing blue decorative emblem"></div>

  <section class="value value--exceed">
    <svg class="value-title" style="left:0;top:0" width="1200" height="220">
      <text class="headline" x="116" y="148" font-size="80" textLength="384" lengthAdjust="spacingAndGlyphs">EXCEED</text>
      <text class="subline" x="115" y="196" font-size="38" textLength="374" lengthAdjust="spacingAndGlyphs">EXPECTATIONS</text>
    </svg>
    <ul class="value-points" style="left:156px;top:218px">
      <li style="top:0">We establish a good understanding of<br>current expectations.</li>
      <li style="top:66px">We provide helpful, honest, and timely<br>feedback.</li>
      <li style="top:132px">We deliver impressive quality.</li>
    </ul>
  </section>

  <section class="value value--empower">
    <svg class="value-title" style="left:0;top:400px" width="1200" height="200">
      <text class="headline" x="628" y="121" font-size="79" textLength="500" lengthAdjust="spacingAndGlyphs">EMPOWER</text>
      <text class="subline" x="626" y="170" font-size="38" textLength="320" lengthAdjust="spacingAndGlyphs">EACH OTHER</text>
    </svg>
    <ul class="value-points" style="left:668px;top:592px">
      <li style="top:0">We are available to help colleagues.</li>
      <li style="top:43px">We are open-minded.</li>
      <li style="top:86px">We seek and share information proactively.</li>
      <li style="top:129px">We respect others’ time.</li>
    </ul>
  </section>

  <section class="value value--execute">
    <svg class="value-title" style="left:0;top:790px" width="1200" height="200">
      <text class="headline" x="116" y="102" font-size="78" textLength="444" lengthAdjust="spacingAndGlyphs">EXECUTE</text>
      <text class="subline" x="116" y="152" font-size="40" textLength="358" lengthAdjust="spacingAndGlyphs">WITH PASSION</text>
    </svg>
    <ul class="value-points" style="left:159px;top:963px">
      <li style="top:0">We embrace change.</li>
      <li style="top:41px">We seek innovative solutions.</li>
      <li style="top:82px">We inspire others with our actions and attitudes.</li>
      <li style="top:123px">We care about success.</li>
      <li style="top:164px">We are confident and humble.</li>
    </ul>
  </section>
</main>
</body>
</html>
```